Design a beautiful book cover for my self help book

The Craft of Hush is a book I've written about how I learnt to quite my mind, rid myself of old pain and stand in my intuition. It's one simple practical tool to find you moment and step into your abundance. We need a cover that reflects this amazing concept! The current cover is attached. It's too dark and not in tune with the market. Please search books with similar content and make design similar yet different.

Target Market(s)

People into self help or motivational content. As well as people suffering from depression, stress, anxiety etc.

Industry/Entity Type

Self Help

Requirements
Must have
• A light airy feel of freedom
Nice to have
• Some sort of linage from current cover
Should not have
• Dark, ambiguous,

```html
<!DOCTYPE html>
<html lang="en">
<head>
<meta charset="utf-8">
<title>The Craft of Hush — Book Cover</title>
<link rel="stylesheet" href="https://fonts.googleapis.com/css2?family=Fraunces:opsz,wght@9..144,600;9..144,700&family=Open+Sans:wght@700&family=Crimson+Text:wght@400&display=swap">
<style>
  :root {
    --teal: #17808f;
    --teal-deep: #136f7d;
    --ink: #2b2b2b;
    --peach: #f6c9a8;
    --peach-light: #fbe4d3;
    --mist: #d9ecef;
    --sky: #a9d3d8;
    --glow: #fffaf2;
  }
  * { margin: 0; padding: 0; box-sizing: border-box; }
  html, body { width: 1200px; height: 886px; overflow: hidden; }
  body { background: #ffffff; }

  .cover {
    position: relative;
    width: 1200px;
    height: 886px;
    overflow: hidden;
    background:
      radial-gradient(circle at 115px 130px, var(--glow) 0, rgba(255,250,242,0.85) 40px, rgba(255,250,242,0) 170px),
      linear-gradient(115deg, var(--peach) 0%, var(--peach-light) 30%, #eaf1ee 50%, var(--mist) 68%, var(--sky) 100%);
  }

  .scenery {
    position: absolute;
    pointer-events: none;
  }
  .scenery--back-foliage {
    left: 0; bottom: 0; width: 640px; height: 360px;
    background: radial-gradient(ellipse at 30% 100%, rgba(255,255,255,0.9) 0, rgba(248,214,190,0.6) 45%, rgba(248,214,190,0) 75%);
  }
  .scenery--front-clouds {
    right: 0; bottom: 0; width: 620px; height: 330px;
    background: radial-gradient(ellipse at 70% 100%, rgba(255,255,255,0.85) 0, rgba(190,224,230,0.6) 45%, rgba(190,224,230,0) 75%);
  }
  .scenery--crescent {
    left: 660px; top: 250px; width: 200px; height: 260px;
    background: radial-gradient(ellipse at 50% 50%, rgba(255,255,255,0.55) 0, rgba(255,255,255,0) 70%);
  }

  .back-blurb {
    position: absolute;
    left: 178px;
    top: 152px;
    width: 318px;
    font-family: "Crimson Text", Georgia, serif;
    font-size: 15.5px;
    line-height: 1.3;
    color: var(--ink);
  }
  .back-blurb .question { text-align: center; margin-bottom: 9px; }
  .back-blurb .body { text-align: justify; margin-bottom: 9px; }
  .back-blurb .closing { text-align: center; }

  .back-website {
    position: absolute;
    left: 200px;
    top: 800px;
    font-family: "Open Sans", Arial, sans-serif;
    font-weight: 700;
    font-size: 16px;
    color: #111;
  }

  .spine-text {
    position: absolute;
    left: 582px;
    font-family: "Open Sans", Arial, sans-serif;
    font-weight: 700;
    font-size: 21px;
    color: var(--teal);
    white-space: nowrap;
    transform: translate(-50%, -50%) rotate(90deg);
  }
  .spine-text--title { top: 366px; }
  .spine-text--author { top: 650px; }

  .front-title {
    position: absolute;
    left: 660px;
    top: 110px;
    width: 520px;
    font-family: "Fraunces", Georgia, serif;
    font-weight: 700;
    color: var(--teal);
    line-height: 0.85;
  }
  .front-title span { display: block; }
  .front-title .the { font-size: 84px; margin-left: 130px; }
  .front-title .craft { font-size: 170px; margin-left: -10px; letter-spacing: -4px; }
  .front-title .of { font-size: 64px; margin-left: 350px; margin-top: -14px; }
  .front-title .hush { font-size: 180px; margin-left: 0; margin-top: -20px; letter-spacing: -3px; color: var(--teal-deep); }

  .front-sparkle {
    position: absolute;
    left: 1030px;
    top: 158px;
    width: 42px;
    height: 56px;
  }

  .front-author {
    position: absolute;
    left: 767px;
    top: 765px;
    font-family: "Open Sans", Arial, sans-serif;
    font-weight: 700;
    font-size: 52px;
    color: var(--teal);
    letter-spacing: -0.5px;
  }
</style>
</head>
<body>
<main class="cover">
  <div class="scenery scenery--back-foliage" role="img" aria-label="Soft pastel clouds and delicate blue and peach foliage"></div>
  <div class="scenery scenery--front-clouds" role="img" aria-label="Pale blue clouds with drifting leaves and bubbles"></div>
  <div class="scenery scenery--crescent" role="img" aria-label="Faint white crescent moon glow"></div>

  <section class="back-blurb">
    <p class="question">Do you think too much?</p>
    <p class="question">Do you overanalyse past events<br>and worry about the future?</p>
    <p class="question">Are you stuck in your head<br>instead of living in the here and now?</p>
    <p class="body">I used to live in a hamster wheel of thought. I was in a constant state of expectation, speculation, judgement, self-annihilation, stress, anxiety and depression. It wasn't until I practised The Craft of Hush that I was able to find true freedom.</p>
    <p class="body">The Craft of Hush is a simple yet powerful tool to help you cut the puppet strings of your internal chatter and release the grip of past traumas. It will help you tame your thoughts and reconnect with your intuition.</p>
    <p class="body closing">Experience the transformative effect of this life-changing practice and embrace a newfound sense of freedom and self-awareness.</p>
  </section>

  <p class="back-website">www.rowanhale.com</p>

  <p class="spine-text spine-text--title">The Craft of Hush</p>
  <p class="spine-text spine-text--author">Rowan Hale</p>

  <h1 class="front-title">
    <span class="the">The</span>
    <span class="craft">Craft</span>
    <span class="of">of</span>
    <span class="hush">Hush</span>
  </h1>

  <svg class="front-sparkle" viewBox="0 0 42 56" aria-hidden="true">
    <path d="M21 0 L25 24 L42 28 L25 32 L21 56 L17 32 L0 28 L17 24 Z" fill="#ffffff"/>
  </svg>

  <p class="front-author">Rowan Hale</p>
</main>
</body>
</html>
```